Business Card Design

Hoping for a black background business card, minimalistic design.
With the Marble Crest logo you created in white.

I would like to include:
My Name and title
Address (street address)
Reception: (phone number)
Fax: (fax number)
Reception: (email address)
Direct email: (email address)
Instagram: (ig handle)

```html
<!DOCTYPE html>
<html lang="en">
<head>
<meta charset="utf-8">
<title>Marble Crest — Business Card</title>
<link rel="stylesheet" href="https://fonts.googleapis.com/css2?family=Lato:wght@400;700;900&display=swap">
<style>
  :root {
    --backdrop: #3a3a3d;
    --card: #1c1c1d;
    --card-edge: #2a2a2b;
    --ink: #ffffff;
    --ink-soft: #e9e9e9;
    --emboss: #101011;
    --ring: #8c8c8e;
  }
  * { box-sizing: border-box; margin: 0; padding: 0; }
  html, body { width: 1200px; height: 913px; overflow: hidden; }
  body {
    background: var(--backdrop);
    font-family: "Lato", sans-serif;
    position: relative;
  }
  .card {
    position: absolute;
    width: 620px;
    height: 354px;
    background: var(--card);
    border-radius: 18px;
    box-shadow: 0 0 0 1px var(--card-edge), 0 14px 30px rgba(0,0,0,0.45);
    overflow: hidden;
  }
  .card--front { left: 60px; top: 70px; }
  .card--back { left: 520px; top: 490px; }

  /* Front */
  .front-brand {
    position: absolute;
    left: 0; right: 0; top: 0; bottom: 0;
    display: flex;
    align-items: center;
    justify-content: center;
    gap: 22px;
  }
  .brand-dot {
    width: 96px; height: 96px;
    border-radius: 50%;
    border: 3px solid var(--emboss);
    box-shadow: 0 1px 0 rgba(255,255,255,0.06);
  }
  .brand-divider {
    width: 1px; height: 110px;
    background: var(--emboss);
  }
  .brand-name {
    font-weight: 400;
    font-size: 44px;
    letter-spacing: 4px;
    color: var(--ink-soft);
    text-transform: uppercase;
  }

  /* Back */
  .back-details {
    position: absolute;
    left: 40px; top: 52px;
    color: var(--ink);
  }
  .back-brand {
    font-size: 34px;
    font-weight: 400;
    letter-spacing: 3px;
    text-transform: uppercase;
    line-height: 1;
  }
  .person-name {
    margin-top: 22px;
    font-size: 30px;
    font-weight: 900;
    line-height: 1;
  }
  .person-title {
    margin-top: 6px;
    font-size: 18px;
  }
  .contact-list {
    list-style: none;
    margin-top: 18px;
    margin-left: 20px;
    font-size: 15px;
    line-height: 21px;
  }
  .contact-list li {
    display: flex;
    align-items: flex-start;
    gap: 10px;
  }
  .contact-icon {
    width: 14px; height: 14px;
    margin-top: 4px;
    flex: none;
    fill: var(--ink);
  }
  .back-ring {
    position: absolute;
    right: 36px; top: 40px;
    width: 270px; height: 270px;
    border-radius: 50%;
    border: 10px solid var(--ring);
    opacity: 0.55;
  }
</style>
</head>
<body>

<section class="card card--front" aria-label="Card front">
  <div class="front-brand">
    <span class="brand-dot"></span>
    <span class="brand-divider"></span>
    <span class="brand-name">Marble Crest</span>
  </div>
</section>

<section class="card card--back" aria-label="Card back">
  <div class="back-ring"></div>
  <div class="back-details">
    <div class="back-brand">Marble Crest</div>
    <div class="person-name">Daniel Reyes</div>
    <div class="person-title">Founder &amp; CEO</div>
    <ul class="contact-list">
      <li>
        <svg class="contact-icon" viewBox="0 0 14 14" aria-hidden="true"><path d="M7 0a5 5 0 0 0-5 5c0 3.6 5 9 5 9s5-5.4 5-9a5 5 0 0 0-5-5zm0 7a2 2 0 1 1 0-4 2 2 0 0 1 0 4z"/></svg>
        <span>Address, City, State<br>Country, Zip 1235</span>
      </li>
      <li>
        <svg class="contact-icon" viewBox="0 0 14 14" aria-hidden="true"><path d="M3 0.5l2.2 2.8-1.3 1.7c.9 1.9 2.3 3.3 4.2 4.2l1.7-1.3 2.8 2.2-1.2 2.4C6 12 2 8 1 1.7z"/></svg>
        <span>(555) 201-4410</span>
      </li>
      <li>
        <svg class="contact-icon" viewBox="0 0 14 14" aria-hidden="true"><path d="M3 0h8v4H3zM1 5h12v6h-2V9H3v2H1zM4 10h6v4H4z"/></svg>
        <span>(555) 201-4411</span>
      </li>
      <li>
        <svg class="contact-icon" viewBox="0 0 14 14" aria-hidden="true"><path d="M0 2h14v1.2L7 8 0 3.2zM0 5l7 4.6L14 5v7H0z"/></svg>
        <span>desk@marblecrest.co</span>
      </li>
      <li>
        <svg class="contact-icon" viewBox="0 0 14 14" aria-hidden="true"><path d="M0 2h14v1.2L7 8 0 3.2zM0 5l7 4.6L14 5v7H0z"/></svg>
        <span>daniel@marblecrest.co</span>
      </li>
      <li>
        <svg class="contact-icon" viewBox="0 0 14 14" aria-hidden="true"><circle cx="7" cy="7" r="5.5" fill="none" stroke="#ffffff" stroke-width="1.6"/></svg>
        <span>@marblecrest.studio</span>
      </li>
    </ul>
  </div>
</section>

</body>
</html>
```